I will ask the design of the business card

We are looking for business card design of the new company "TORVIK QUANTA WORKS LLC." Based in Azerbaijan.
In case
We are working on Azerbaijan to set up the first exchange of crypto currencies.

The key currency used in exchanges is called "MELDA".
In case
We are doing project to make crypto currency infrastructure.

We provide state-of-the-art technology to the world.

```html
<!DOCTYPE html>
<html lang="en">
<head>
<meta charset="utf-8">
<title>Torvik Quanta Works LLC. — Business Card</title>
<link href="https://fonts.googleapis.com/css2?family=Michroma&family=Montserrat:wght@500;600&display=swap" rel="stylesheet">
<style>
  :root {
    --stage: #2b2b30;
    --card: #0b0b0d;
    --blue: #2f5fc4;
    --orange: #f08a1c;
    --silver: #d9d9dc;
    --white: #f4f4f4;
    --ring: #5a5a60;
  }
  * { margin: 0; padding: 0; box-sizing: border-box; }
  html, body { width: 1200px; height: 902px; overflow: hidden; }
  body {
    background: var(--stage);
    display: flex;
    flex-direction: column;
    align-items: center;
    justify-content: center;
    gap: 36px;
    font-family: "Montserrat", sans-serif;
  }
  .card {
    width: 700px;
    height: 400px;
    background: var(--card);
    border-radius: 22px;
    position: relative;
    overflow: hidden;
    box-shadow: 0 10px 30px rgba(0,0,0,.45);
  }

  /* Front */
  .card--front {
    display: flex;
    align-items: center;
    justify-content: center;
    gap: 30px;
  }
  .brand-dot {
    width: 120px; height: 120px;
    border-radius: 50%;
    border: 6px solid var(--blue);
  }
  .brand-name {
    font-family: "Michroma", sans-serif;
    color: var(--blue);
    font-size: 34px;
    line-height: 1.25;
    letter-spacing: 1px;
  }

  /* Back */
  .card--back .details {
    position: absolute;
    left: 56px;
    top: 60px;
  }
  .card--back .brand-name {
    color: var(--silver);
    font-size: 30px;
    margin-bottom: 34px;
  }
  .person-name {
    font-family: "Michroma", sans-serif;
    color: var(--white);
    font-size: 22px;
    letter-spacing: 1px;
  }
  .person-role {
    color: var(--orange);
    font-weight: 600;
    font-size: 12px;
    letter-spacing: 1.5px;
    margin-top: 4px;
    margin-bottom: 18px;
  }
  .address {
    color: var(--white);
    font-size: 14px;
    line-height: 1.5;
    margin-bottom: 14px;
  }
  .contact-list { list-style: none; }
  .contact-list li {
    display: flex;
    align-items: center;
    gap: 12px;
    color: var(--white);
    font-size: 14px;
    line-height: 1.75;
  }
  .contact-list svg { width: 14px; height: 14px; fill: var(--orange); flex: none; }
  .mark-circle {
    position: absolute;
    right: -40px;
    top: 40px;
    width: 320px; height: 320px;
    border-radius: 50%;
    border: 14px solid var(--ring);
  }
</style>
</head>
<body>
  <section class="card card--front">
    <div class="brand-dot"></div>
    <div class="brand-name">TORVIK QUANTA<br>WORKS LLC.</div>
  </section>

  <section class="card card--back">
    <div class="mark-circle"></div>
    <div class="details">
      <div class="brand-name">TORVIK QUANTA<br>WORKS LLC.</div>
      <div class="person-name">RASIM KAVEL</div>
      <div class="person-role">MANAGING DIRECTOR</div>
      <div class="address">14 Nizami Street, Suite 320<br>Baku, AZ1000</div>
      <ul class="contact-list">
        <li><svg viewBox="0 0 16 16"><path d="M3 1l3 3-1.5 2a9 9 0 0 0 5.5 5.5L12 10l3 3-2 2C7 15 1 9 1 3z"/></svg>+994 12 555 0143</li>
        <li><svg viewBox="0 0 16 16"><path d="M4 1h8v4H4zM1 6h14v6h-3v3H4v-3H1zM5 10v4h6v-4z"/></svg>+994 12 555 0187</li>
        <li><svg viewBox="0 0 16 16"><path d="M1 3h14v10H1zM2 4l6 5 6-5v1L8 10 2 5z" fill-rule="evenodd"/></svg>info@torvikquanta.az</li>
        <li><svg viewBox="0 0 16 16"><path d="M8 1a7 7 0 1 0 0 14A7 7 0 0 0 8 1zm0 1.5c1 1.2 1.6 3 1.7 4.7H6.3C6.4 5.5 7 3.7 8 2.5zM6.3 8.8h3.4c-.1 1.7-.7 3.5-1.7 4.7-1-1.2-1.6-3-1.7-4.7zM2.6 7.2h2.2c.1-1.5.5-2.9 1.1-4a5.5 5.5 0 0 0-3.3 4zm0 1.6a5.5 5.5 0 0 0 3.3 4c-.6-1.1-1-2.5-1.1-4zm8.6 0c-.1 1.5-.5 2.9-1.1 4a5.5 5.5 0 0 0 3.3-4zm0-1.6h2.2a5.5 5.5 0 0 0-3.3-4c.6 1.1 1 2.5 1.1 4z"/></svg>www.torvikquanta.az</li>
      </ul>
    </div>
  </section>
</body>
</html>
```